QUOTE Graphics for Summer Challenge

I would like to put these quotes over one of the pictures attached; For Instagram, use new size: 4:5 (1080 x 1350 pixels). One Quote per picture, and I want the quote to be bold or easy to read as well. I provided a few reference graphics that I really like as examples below.
All of the pictures are attached; you can pick any photo and add one quote to it; but no stock photography
All the quotes are in the attached WORD document

```html
<!DOCTYPE html>
<html lang="en">
<head>
<meta charset="utf-8">
<title>Summer Challenge Quote Graphics</title>
<link href="https://fonts.googleapis.com/css2?family=Marcellus&family=Roboto:wght@400;500;700;900&display=swap" rel="stylesheet">
<style>
  :root{
    --board:#d4d5d7;
    --white:#ffffff;
    --coral:#f47b7d;
    --blush:#fde6ee;
    --band-top:#f27a7f;
    --band-bottom:#7b3a6d;
    --plum:#7a3a6b;
    --sea:#3d5f88;
    --night:#0d1828;
    --lavender-top:#655789;
    --lavender-mid:#b7a3c6;
    --lavender-low:#e2cfdf;
    --rose-band:rgba(194,92,126,.78);
    --ink-dark:#1d1d1f;
  }
  *{margin:0;padding:0;box-sizing:border-box}
  html,body{width:1007px;height:1200px;overflow:hidden;background:var(--board)}
  body{position:relative;font-family:"Roboto",Arial,sans-serif;color:var(--white)}
  .post{position:absolute;width:405px;height:508px;overflow:hidden}
  .post--jumpstart{left:70px;top:63px;background:var(--blush)}
  .post--cravings{left:532px;top:63px}
  .post--lifeline{left:70px;top:627px}
  .post--bloated{left:532px;top:627px}
  .photo{position:absolute}
  .abs{position:absolute}

  /* Post 1 */
  .jumpstart__edge{left:0;top:0;width:17px;height:100%;background:#fbeef3}
  .jumpstart__band{left:17px;top:0;width:240px;height:100%;background:linear-gradient(180deg,var(--band-top) 0%,#c95479 45%,var(--band-bottom) 100%)}
  .jumpstart__photo{left:136px;top:96px;width:269px;height:412px;border-radius:130px 130px 0 0;background:radial-gradient(ellipse at 55% 35%,#6b4331 0%,#8a5a3f 45%,#b07a55 75%,rgba(176,122,85,0) 100%)}
  .jumpstart__quote{left:35px;top:32px;text-transform:uppercase;line-height:1}
  .jumpstart__small{font-size:18px;font-weight:400;letter-spacing:.5px;line-height:19px}
  .jumpstart__big{font-size:33px;font-weight:900;letter-spacing:-.5px;line-height:29px}

  .cta-tag{position:absolute;background:var(--coral);color:var(--white);font-weight:700;display:flex;align-items:center}
  .cta-keyword{position:absolute;font-weight:700;line-height:1}
  .cta-note{position:absolute;font-weight:400;line-height:1;white-space:nowrap}

  /* Post 2 */
  .cravings__photo{inset:0;background:linear-gradient(180deg,var(--plum) 0%,#6a4a7a 18%,#3f6690 38%,var(--sea) 60%,#1b2c45 82%,var(--night) 100%)}
  .serif-quote{font-family:"Marcellus",Georgia,serif;text-transform:uppercase;font-weight:400}
  .cravings__quote{right:23px;top:52px;text-align:right;font-size:37px;line-height:42px;letter-spacing:1px}
  .cravings__sub{right:22px;top:269px;text-align:right;font-size:16px;line-height:20px;text-transform:uppercase}

  /* Post 3 */
  .lifeline__sky{inset:0;background:linear-gradient(180deg,var(--lavender-top) 0%,#8a78a8 25%,var(--lavender-mid) 45%,var(--lavender-low) 62%,#e9d8e2 72%)}
  .lifeline__photo{left:0;top:300px;width:405px;height:208px;background:linear-gradient(180deg,rgba(233,216,226,0) 0%,#b7c7cc 35%,#8fb7c4 60%,#9fc4ce 80%,#e8ddd2 100%)}
  .lifeline__figure{left:175px;top:180px;width:230px;height:328px;border-radius:110px 110px 20px 20px;background:radial-gradient(ellipse at 50% 40%,#5a3a2a 0%,#8a5a3c 50%,rgba(138,90,60,0) 78%)}
  .lifeline__quote{left:0;width:405px;top:36px;text-align:center;font-size:23px;font-weight:700;line-height:24.5px;text-transform:uppercase}

  /* Post 4 */
  .bloated__photo{inset:0;background:linear-gradient(180deg,#b9b9b9 0%,#8c8c8c 35%,#5f5f5f 60%,#3a3a3a 80%,#262626 100%)}
  .bloated__band{left:0;top:260px;width:405px;height:162px;background:var(--rose-band)}
  .bloated__quote{left:0;width:405px;top:277px;text-align:center;font-size:30px;line-height:36px;letter-spacing:1.5px}
  .bloated__sub{left:0;width:405px;top:391px;text-align:center;font-size:15px;text-transform:uppercase}
</style>
</head>
<body>

<section class="post post--jumpstart">
  <div class="abs jumpstart__edge"></div>
  <div class="abs jumpstart__band"></div>
  <div class="photo jumpstart__photo" role="img" aria-label="Woman in a brown crochet swimsuit posing with hand on hip"></div>
  <div class="abs jumpstart__quote">
    <div class="jumpstart__small">If you feel<br>like you've</div>
    <div class="jumpstart__big" style="margin-top:4px">Let<br>yourself<br>go lately,</div>
    <div class="jumpstart__small" style="margin-top:3px">This is your</div>
    <div class="jumpstart__big">Jumpstart.</div>
  </div>
  <div class="cta-tag" style="left:35px;top:426px;width:156px;height:23px;font-size:13.5px;padding-left:8px">Comment</div>
  <div class="cta-keyword" style="left:35px;top:456px;font-size:15px">SUMMER</div>
  <div class="cta-note" style="left:35px;top:473px;font-size:9px">to join the Golden Summer Slimdown</div>
</section>

<section class="post post--cravings">
  <div class="photo cravings__photo" role="img" aria-label="Smiling woman in a sheer cover-up standing in front of the sea at dusk"></div>
  <div class="abs serif-quote cravings__quote">Cravings,<br>belly fat,<br>and<br>water<br>weight?</div>
  <div class="abs cravings__sub">Say goodbye<br>in 30 days</div>
  <div class="cta-tag" style="left:273px;top:389px;width:111px;height:17px;font-size:10px;justify-content:center">COMMENT</div>
  <div class="cta-keyword" style="right:22px;top:413px;font-size:15px">SUMMER</div>
  <div class="cta-note" style="right:22px;top:429px;font-size:9px">to join the Golden Summer Slimdown</div>
</section>

<section class="post post--lifeline">
  <div class="photo lifeline__sky" role="img" aria-label="Woman in a leopard print bikini sitting poolside, smiling over her shoulder"></div>
  <div class="abs lifeline__photo"></div>
  <div class="abs lifeline__figure"></div>
  <div class="abs lifeline__quote">The scale keeps<br>climbing and<br>nothing’s working?<br>This challenge is<br>your lifeline.</div>
  <div class="cta-tag" style="left:28px;top:200px;width:98px;height:22px;font-size:13.5px;padding-left:7px">Comment</div>
  <div class="cta-keyword" style="left:28px;top:238px;font-size:20px">GOLDEN</div>
  <div class="cta-note" style="left:28px;top:262px;font-size:13px">to join now!</div>
</section>

<section class="post post--bloated">
  <div class="photo bloated__photo" role="img" aria-label="Black and white photo of a smiling woman in a cut-out swimsuit on a hillside terrace"></div>
  <div class="abs bloated__band"></div>
  <div class="abs serif-quote bloated__quote">Feeling bloated,<br>sluggish,<br>and too big?</div>
  <div class="abs bloated__sub">Your detox starts now</div>
  <div class="cta-tag" style="left:29px;top:454px;width:111px;height:23px;font-size:13.5px;padding-left:10px">COMMENT</div>
  <div class="cta-keyword" style="right:29px;top:460px;font-size:15px">SUMMER</div>
  <div class="cta-note" style="right:29px;top:476px;font-size:9px">to join the Golden Summer Slimdown</div>
</section>

</body>
</html>
```